Visitenkarte für Ergotherapiepraxis
Zielgruppe
Wir arbeiten mit Kindern und Erwachsene jeden Alters.
Diese Personen kommen mit Beeinträchtigungen (körperlich, seelisch, schulisch) im täglichen Leben zu uns. Wir unterstützen unsere Patienten die Beeinträchtigungen zu verringern oder zu kompensieren und so den Alltag besser bewältigen zu können.
Aufgabenstellung
Ein Design was Kinder und Erwachsene anspricht, aber nicht zu verspielt wirkt. Es soll vertrauenserweckend sein. Eventuell sollte die Visitenkarte ein "aufgehendes oder erblühendes oder aufsteigendes" Element enthalten (=zu Beginn war die Beeinträchtigung dann steigt die Lebensqualität als Folge der Behandlung)
Daten vorn:
Ergotherapiepraxis

```html
<!DOCTYPE html>
<html lang="de">
<head>
<meta charset="utf-8">
<title>Visitenkarte Ergotherapiepraxis</title>
<link rel="stylesheet" href="https://fonts.googleapis.com/css2?family=Didact+Gothic&display=swap">
<style>
  :root {
    --page-bg: #ffffff;
    --card-bg: #ffffff;
    --card-border: #d9d9d9;
    --brand-red: #d2261c;
    --brand-pink: #c65aaa;
    --brand-green: #8cc63f;
    --text-dark: #1a1a1a;
  }
  * { box-sizing: border-box; margin: 0; padding: 0; }
  html, body {
    width: 1052px;
    height: 1200px;
    overflow: hidden;
    background: var(--page-bg);
    font-family: "Didact Gothic", "Century Gothic", sans-serif;
  }
  .canvas { position: relative; width: 1052px; height: 1200px; }
  .card {
    position: absolute;
    left: 19px;
    width: 1014px;
    height: 564px;
    background: var(--card-bg);
    border: 2px solid var(--card-border);
  }
  .card--front { top: 19px; }
  .card--back { top: 617px; }

  .brand-mark {
    position: absolute;
    display: flex;
    flex-direction: column;
    align-items: center;
    gap: 26px;
  }
  .card--front .brand-mark { left: 65px; top: 130px; width: 430px; }
  .card--back .brand-mark { left: 304px; top: 90px; width: 406px; }
  .brand-dot {
    width: 150px;
    height: 150px;
    border-radius: 50%;
    background: var(--brand-green);
  }
  .brand-name {
    font-size: 40px;
    line-height: 1;
    color: var(--brand-green);
    white-space: nowrap;
  }

  .practice-owner {
    position: absolute;
    right: 60px;
    top: 118px;
    font-size: 62px;
    font-weight: 400;
    color: var(--brand-red);
    line-height: 1;
    letter-spacing: 0.5px;
  }
  .practice-type {
    position: absolute;
    right: 60px;
    top: 195px;
    font-size: 31px;
    color: var(--brand-pink);
    line-height: 1;
  }
  .contact {
    position: absolute;
    right: 60px;
    top: 378px;
    font-size: 36px;
    font-style: italic;
    color: var(--text-dark);
    text-align: right;
    line-height: 50px;
  }
  .therapist-label {
    position: absolute;
    left: 0;
    right: 0;
    top: 425px;
    text-align: center;
    font-size: 66px;
    line-height: 1;
  }
  .therapist-label .word-red { color: var(--brand-red); }
  .therapist-label .word-pink { color: var(--brand-pink); }
</style>
</head>
<body>
  <main class="canvas">
    <section class="card card--front">
      <div class="brand-mark">
        <span class="brand-dot"></span>
        <span class="brand-name">Marlene Quast</span>
      </div>
      <h1 class="practice-owner">Marlene Quast</h1>
      <p class="practice-type">Ergotherapiepraxis</p>
      <address class="contact">
        Am Lindenweg 12<br>
        14820 Feldau, OT Rohrbach<br>
        Tel. 033845/27190
      </address>
    </section>

    <section class="card card--back">
      <div class="brand-mark">
        <span class="brand-dot"></span>
        <span class="brand-name">Marlene Quast</span>
      </div>
      <p class="therapist-label"><span class="word-red">Behandelnder</span> <span class="word-pink">Therapeut</span></p>
    </section>
  </main>
</body>
</html>
```